Fahrzeugbeschriftung für Informationselektronik
Zielgruppe
SAT-Anlagen, Antennenanlagen, Kabelfernsehen
Telekommunikation, Internet, Netzwerktechnik
Radio- und Fernsehtechnik
Alarmanlagen, Videoüberwachung
Elektrokleinreparaturen
Zielgruppe: Hauptsächlich Privatleute
Beratung, Planung, Neuinstallation und hauptsächlich Service und Reparaturen
Aufgabenstellung
auffällig, anders nicht nur Schrift und Logo fertig
WALDEK Informationselektronik
Master Professional

```html
<!DOCTYPE html>
<html lang="de">
<head>
<meta charset="utf-8">
<title>WALDEK Informationstechnik – Fahrzeugbeschriftung</title>
<link href="https://fonts.googleapis.com/css2?family=Barlow+Semi+Condensed:wght@400;500;600&display=swap" rel="stylesheet">
<style>
  :root{
    --wrap-white:#f7f7f7;
    --band-grey:#c9c9c9;
    --brand-blue:#4f73b8;
    --logo-grey:#8c8c8c;
    --ink:#222428;
    --navy:#1f2a44;
    --on-blue:#ffffff;
  }
  html,body{margin:0;padding:0;overflow:hidden;}
  body{width:1200px;height:523px;background:#ffffff;}
  .wrap{width:1200px;height:523px;display:block;font-family:"Barlow Semi Condensed",sans-serif;}
  .band-grey{fill:var(--band-grey);}
  .area-white{fill:var(--wrap-white);}
  .area-blue{fill:var(--brand-blue);}
  .web{fill:var(--ink);font-size:30px;font-weight:500;}
  .brand-name{fill:var(--logo-grey);font-size:90px;font-weight:500;}
  .brand-line{fill:var(--logo-grey);font-size:31px;font-weight:400;}
  .brand-sub{fill:var(--logo-grey);font-size:30px;font-weight:400;}
  .address{fill:var(--ink);font-size:9.5px;font-weight:500;}
  .phone{fill:var(--ink);font-size:28px;font-weight:500;}
  .service{fill:var(--on-blue);font-size:11.5px;font-weight:500;}
  .tagline{fill:var(--navy);font-size:24px;font-weight:500;}
</style>
</head>
<body>
<svg class="wrap" viewBox="0 0 1200 523" xmlns="http://www.w3.org/2000/svg">
  <rect class="area-white" x="0" y="0" width="1200" height="523"/>
  <polygon class="band-grey" points="0,0 1190,0 0,277"/>
  <polygon class="area-blue" points="325,523 325,370 1200,143 1200,523"/>

  <text class="web" transform="translate(582,132) rotate(-14.7)" textLength="295" lengthAdjust="spacingAndGlyphs">www.waldek-info.de</text>

  <text class="brand-name" transform="translate(640,215) rotate(-13.7)" textLength="440" lengthAdjust="spacingAndGlyphs">WALDEK</text>
  <text class="brand-line" transform="translate(658,246) rotate(-16.5)" textLength="440" lengthAdjust="spacingAndGlyphs">INFORMATIONSTECHNIK</text>
  <text class="brand-sub" transform="translate(850,227) rotate(-14.8)" textLength="250" lengthAdjust="spacingAndGlyphs">Meisterbetrieb</text>

  <g class="address">
    <text x="292" y="254">INFORMATIONSTECHNIK WALDEK</text>
    <text x="292" y="268">Meisterbetrieb</text>
    <text x="292" y="282">Lindenallee 12,</text>
    <text x="292" y="296">D-50999 Musterstadt</text>
  </g>

  <text class="phone" transform="translate(336,363) rotate(-16.2)" textLength="280" lengthAdjust="spacingAndGlyphs">mob. (0170) 12 34 567</text>

  <g class="service">
    <text x="567" y="328">Sat-Kabel-Antennentechnik</text>
    <text x="567" y="349">Alarm- &amp; Sicherheitstechnik</text>
    <text x="567" y="370">Daten- &amp; Netzwerktechnik</text>
    <text x="748" y="325">Gebäudekommunikation</text>
    <text x="748" y="346">Unterhaltungselektronik</text>
    <text x="748" y="367">Videoüberwachung</text>
  </g>

  <text class="tagline" x="364" y="418" textLength="479" lengthAdjust="spacing">BERATUNG | VERKAUF | MONTAGE | SERVICE</text>
</svg>
</body>
</html>
```